Business Card Design needed - Something Awesome!

Need a business card designed. Company is "Harbor Vane Consulting" we do consulting and also have sales automation technology.
I'm going to use thick stock or metal, something really nice... I was thinking about a QR Code on the back that would just upload my contact info to the persons contact, etc -

This is a Strategy Company with a tech feel. I'm open to ideas but really want this to be nice!

I need a template that should include:

Name | Position or Title
D: 987.654.3210
www.harborvaneconsulting.example

I'm going to attach my contact so you can use that one, I need to get this printed.

Target Market(s)

Small to mid size customers, Entrepreneurs etc.

Industry/Entity Type

Consulting, Tech, Private Equity.

Contact Information for Business Card

Name, Phone, Maybe email, URL

Font styles to use
Sans Serif

Colors

Designer to choose only greyscale colors for use in the design.

Requirements
Must have
• Fresh, Clean, stand out from the crowd - will be on thick stock or metal.
Nice to have
• Clean, simple yet impactful.
Should not have
• Not cartoonish

```html
<!DOCTYPE html>
<html lang="en">
<head>
<meta charset="utf-8">
<title>Harbor Vane Consulting — Business Card</title>
<link rel="stylesheet" href="https://fonts.googleapis.com/css2?family=Inter:wght@400;500;700&display=swap">
<style>
  :root {
    --canvas: #d6d6d6;
    --card: #f1f1ef;
    --card-edge: #111111;
    --ink: #0e0e0e;
    --ink-soft: #7a7a7a;
    --rule: #cfcfcc;
  }
  * { margin: 0; padding: 0; box-sizing: border-box; }
  html, body {
    width: 1200px;
    height: 1051px;
    overflow: hidden;
    background: var(--canvas);
    font-family: "Inter", sans-serif;
  }
  .sheet {
    width: 1200px;
    height: 1051px;
    display: flex;
    flex-direction: column;
    align-items: center;
    justify-content: center;
    gap: 64px;
  }
  .card {
    width: 700px;
    height: 400px;
    background: var(--card);
    border-bottom: 4px solid var(--card-edge);
    box-shadow: 0 18px 40px rgba(0,0,0,0.14);
    position: relative;
  }
  /* Front: wordmark */
  .card-front {
    display: flex;
    align-items: center;
    justify-content: center;
  }
  .wordmark {
    font-weight: 500;
    font-size: 64px;
    letter-spacing: 0.02em;
    color: var(--ink);
  }
  /* Back: contact details */
  .card-back {
    display: flex;
    align-items: center;
    justify-content: center;
    gap: 26px;
  }
  .identity {
    text-align: right;
  }
  .identity-name {
    font-weight: 700;
    font-size: 20px;
    letter-spacing: 0.01em;
    text-transform: uppercase;
    color: var(--ink);
  }
  .identity-title {
    font-weight: 400;
    font-size: 15px;
    color: var(--ink-soft);
    margin-top: 4px;
  }
  .divider {
    width: 1px;
    height: 86px;
    background: var(--rule);
  }
  .contact-list {
    list-style: none;
    display: flex;
    flex-direction: column;
    gap: 5px;
  }
  .contact-item {
    display: flex;
    align-items: center;
    gap: 8px;
    font-size: 15px;
    color: var(--ink-soft);
  }
  .contact-icon {
    width: 13px;
    height: 13px;
    fill: var(--ink);
    flex: none;
  }
</style>
</head>
<body>
<main class="sheet">
  <section class="card card-front" aria-label="Card front">
    <h1 class="wordmark">HARBOR VANE</h1>
  </section>

  <section class="card card-back" aria-label="Card back">
    <div class="identity">
      <p class="identity-name">Dorian K. Whitfield</p>
      <p class="identity-title">Founder / CEO</p>
    </div>
    <span class="divider"></span>
    <ul class="contact-list">
      <li class="contact-item">
        <svg class="contact-icon" viewBox="0 0 24 24" aria-hidden="true"><path d="M6.6 10.8a15.1 15.1 0 0 0 6.6 6.6l2.2-2.2a1 1 0 0 1 1-.25 11.4 11.4 0 0 0 3.6.57 1 1 0 0 1 1 1V20a1 1 0 0 1-1 1A17 17 0 0 1 3 4a1 1 0 0 1 1-1h3.5a1 1 0 0 1 1 1c0 1.25.2 2.45.57 3.57a1 1 0 0 1-.25 1z"/></svg>
        987.654.3210
      </li>
      <li class="contact-item">
        <svg class="contact-icon" viewBox="0 0 24 24" aria-hidden="true"><path d="M2 5h20v14H2z M2 5l10 8 10-8" fill="none" stroke="#0e0e0e" stroke-width="0"/><path d="M2 6.2V19h20V6.2l-10 7.6z M3.2 5h17.6L12 11.7z"/></svg>
        info@harborvaneconsulting.example
      </li>
      <li class="contact-item">
        <svg class="contact-icon" viewBox="0 0 24 24" aria-hidden="true"><path d="M12 2a10 10 0 1 0 0 20 10 10 0 0 0 0-20zm0 2c.9 0 2.2 1.9 2.7 5H9.3C9.8 5.9 11.1 4 12 4zM4.3 11h3a18 18 0 0 0 0 2h-3a8 8 0 0 1 0-2zm5 0h5.4a16 16 0 0 1 0 2H9.3a16 16 0 0 1 0-2zm7.4 0h3a8 8 0 0 1 0 2h-3a18 18 0 0 0 0-2zM9.3 15h5.4c-.5 3.1-1.8 5-2.7 5s-2.2-1.9-2.7-5z"/></svg>
        www.harborvaneconsulting.example
      </li>
    </ul>
  </section>
</main>
</body>
</html>
```